Biz Card Physical Therapy Company
Lorimer Physical Therapy
Bright & Fun-filled
Darnell Okoro, PT, CIMT, CSCS
Director
4172 W Fenwick Ave,
Signal Hill, CA 90755
LorimerTherapy@quillpost.com
CA PT 61803
Please feel free to move the logo to the side of the tag-line, or however you may see fit
vector logo file

```html
<!DOCTYPE html>
<html lang="en">
<head>
<meta charset="utf-8">
<title>Lorimer Physical Therapy — Stationery</title>
<link href="https://fonts.googleapis.com/css2?family=Cinzel:wght@400;700&family=Open+Sans:wght@400;600&display=swap" rel="stylesheet">
<style>
  :root{
    --bg:#efe7da;
    --paper:#ffffff;
    --green:#3f8a2e;
    --green-deep:#1f5a1c;
    --green-light:#7dbb4c;
    --ink:#4a4a4a;
    --muted:#8a8a8a;
    --faint:#eef0ec;
    --flap:#2e2e2e;
    --label:#6b5a45;
  }
  *{box-sizing:border-box;margin:0;padding:0}
  html,body{width:1200px;height:446px;overflow:hidden}
  body{background:var(--bg);position:relative;font-family:"Open Sans",Arial,sans-serif;color:var(--ink)}
  .piece{position:absolute;background:var(--paper);box-shadow:0 2px 5px rgba(0,0,0,.18);overflow:hidden}
  .label{position:absolute;font-family:"Cinzel",Georgia,serif;font-size:7px;letter-spacing:.6px;color:var(--label);text-transform:uppercase}
  .brand{font-family:"Cinzel",Georgia,serif;font-weight:700;color:var(--green);line-height:1.05;display:flex;align-items:center;gap:4px}
  .brand .dot{display:inline-block;border-radius:50%;background:var(--green-light)}
  .brand small{display:block;font-weight:700;font-size:.55em;letter-spacing:.3px}
  .watermark{position:absolute;font-family:"Cinzel",Georgia,serif;font-weight:700;color:var(--faint);white-space:nowrap}
  .band{position:absolute;left:0;right:0;background:linear-gradient(180deg,var(--green-light),var(--green-deep))}
  .contact{font-size:4px;line-height:1.45;color:var(--muted)}

  /* business cards */
  .card-front{left:20px;top:216px;width:74px;height:52px;background:radial-gradient(circle at 50% 45%,var(--green-light),var(--green-deep));display:flex;align-items:center;justify-content:center}
  .card-front .brand{color:#fff;font-size:7px}
  .card-front .brand .dot{background:#fff;width:5px;height:5px}
  .card-back{left:20px;top:322px;width:74px;height:62px;padding:7px}
  .card-back .brand{font-size:6px}
  .card-back .brand .dot{width:4px;height:4px}
  .card-back .contact{margin-top:5px;font-size:3.4px}
  .card-back .band{bottom:0;height:5px}

  /* letterheads */
  .letterhead{top:19px;width:221px;height:401px}
  .lh-1{left:163px}
  .lh-2{left:413px}
  .letterhead .brand{position:absolute;left:14px;top:14px;font-size:8px}
  .letterhead .brand .dot{width:6px;height:6px}
  .lh-1 .contact{position:absolute;right:14px;top:14px;text-align:left}
  .letterhead .watermark{left:36px;top:178px;font-size:42px}
  .letterhead .band{bottom:0;height:14px}
  .lh-2 .contact{position:absolute;left:0;right:0;bottom:22px;text-align:center}

  /* envelopes */
  .envelope{left:845px;width:283px}
  .env-back-green{top:24px;height:125px}
  .env-back-green .flap{position:absolute;left:0;right:0;top:0;height:50px;background:linear-gradient(180deg,var(--green-deep),var(--green-light))}
  .env-back-dark{top:158px;height:130px}
  .env-back-dark svg{position:absolute;left:0;top:0}
  .env-back-dark .brand{position:absolute;left:50%;top:70px;transform:translateX(-50%);font-size:7px}
  .env-back-dark .brand .dot{width:5px;height:5px}
  .env-front{top:300px;height:108px}
  .env-front .brand{position:absolute;left:12px;top:10px;font-size:6px}
  .env-front .brand .dot{width:4px;height:4px}
  .env-front .contact{position:absolute;left:12px;top:28px;font-size:3.4px}
  .env-front .watermark{right:14px;top:30px;font-size:30px}
  .env-front .band{bottom:0;height:9px}
</style>
</head>
<body>
  <span class="label" style="left:14px;top:186px">Stationery Concepts</span>

  <div class="piece card-front">
    <div class="brand"><span class="dot"></span><span>Lorimer<small>Physical Therapy</small></span></div>
  </div>
  <span class="label" style="left:18px;top:276px;font-size:5px">Business Card Front</span>

  <div class="piece card-back">
    <div class="brand"><span class="dot"></span><span>Lorimer<small>Physical Therapy</small></span></div>
    <div class="contact">
      Darnell Okoro, PT, CIMT, CSCS<br>Director<br>4172 W Fenwick Ave, Signal Hill, CA 90755<br>LorimerTherapy@quillpost.com<br>CA PT 61803
    </div>
    <div class="band"></div>
  </div>
  <span class="label" style="left:18px;top:400px;font-size:5px">Business Card Back</span>

  <div class="piece letterhead lh-1">
    <div class="brand"><span class="dot"></span><span>Lorimer<small>Physical Therapy</small></span></div>
    <div class="contact">4172 W Fenwick Ave<br>Signal Hill, CA 90755<br>T (562) 555-0148<br>LorimerTherapy@quillpost.com</div>
    <div class="watermark">Lorimer</div>
    <div class="band"></div>
  </div>
  <span class="label" style="left:243px;top:428px;font-size:5px">Letterhead Option 1</span>

  <div class="piece letterhead lh-2">
    <div class="brand"><span class="dot"></span><span>Lorimer<small>Physical Therapy</small></span></div>
    <div class="watermark">Lorimer</div>
    <div class="contact">4172 W Fenwick Ave, Signal Hill, CA 90755 · T (562) 555-0148 · LorimerTherapy@quillpost.com</div>
    <div class="band"></div>
  </div>
  <span class="label" style="left:493px;top:428px;font-size:5px">Letterhead Option 2</span>

  <div class="piece envelope env-back-green"><div class="flap"></div></div>

  <div class="piece envelope env-back-dark">
    <svg width="283" height="130" viewBox="0 0 283 130"><path d="M0 0H283V14Q141 62 0 14Z" fill="var(--flap)"/></svg>
    <div class="brand"><span class="dot"></span><span>Lorimer</span></div>
  </div>

  <div class="piece envelope env-front">
    <div class="brand"><span class="dot"></span><span>Lorimer<small>Physical Therapy</small></span></div>
    <div class="contact">4172 W Fenwick Ave<br>Signal Hill, CA 90755</div>
    <div class="watermark">Lorimer</div>
    <div class="band"></div>
  </div>
  <span class="label" style="left:950px;top:428px;font-size:5px">Envelope Option 1</span>
</body>
</html>
```